Print and E-book Personal Injury Front and Back Book Cover

I need a book cover for a personal injury law firm book titled "Rising Past the Wreck" with the subtitle "Decoding the Accident Claim Process." The book cover should have an image. This isas a lead generation book designed to be give to potential clients to have them sign as new clients.

Target Market(s)

Potential New Clients Looking For a Personal Injury Attorney

Industry/Entity Type

Legal

Requirements
Must have
• Title and some type of image or images

```html
<!DOCTYPE html>
<html lang="en">
<head>
<meta charset="utf-8">
<title>Rising Past the Wreck — Book Cover</title>
<link href="https://fonts.googleapis.com/css2?family=Montserrat:wght@500;600;700&family=Source+Serif+4:wght@400&display=swap" rel="stylesheet">
<style>
  :root {
    --stage: #c9d0d2;
    --cover-top: #f1f4f7;
    --cover-bottom: #d6e1ec;
    --ink: #23252a;
    --accent: #d9830a;
    --photo-edge: #dfe6ee;
    --photo-mid: #8f9fb3;
    --photo-core: #2e2623;
  }
  * { margin: 0; padding: 0; box-sizing: border-box; }
  html, body {
    width: 1066px;
    height: 1200px;
    overflow: hidden;
    background: var(--stage);
  }
  .book-cover {
    position: absolute;
    left: 153px;
    top: 28px;
    width: 760px;
    height: 1143px;
    background: linear-gradient(180deg, var(--cover-top) 0%, #f7f9fb 40%, var(--cover-bottom) 100%);
    overflow: hidden;
    box-shadow: 0 6px 22px rgba(0,0,0,0.18);
  }
  .title {
    position: absolute;
    left: 0;
    width: 100%;
    font-family: "Montserrat", sans-serif;
    font-weight: 700;
    letter-spacing: -3px;
    line-height: 1;
    white-space: nowrap;
    text-align: center;
  }
  .title-small {
    font-family: "Source Serif 4", serif;
    font-weight: 400;
    font-size: 52px;
    letter-spacing: 0;
    color: var(--ink);
    margin-right: 4px;
  }
  .title-line-one { top: 95px; font-size: 122px; color: var(--ink); padding-left: 10px; }
  .title-line-two { top: 222px; font-size: 122px; color: var(--accent); padding-left: 30px; }
  .cover-photo {
    position: absolute;
    left: 0;
    top: 378px;
    width: 760px;
    height: 446px;
    background:
      radial-gradient(ellipse 34% 40% at 56% 58%, var(--photo-core) 0%, #4a3e38 45%, rgba(143,159,179,0) 100%),
      linear-gradient(180deg, var(--photo-edge) 0%, var(--photo-mid) 55%, var(--photo-edge) 100%);
  }
  .subtitle {
    position: absolute;
    left: 0;
    top: 852px;
    width: 100%;
    text-align: center;
    font-family: "Montserrat", sans-serif;
    font-weight: 500;
    font-size: 32px;
    line-height: 45px;
    letter-spacing: 0.42em;
    color: var(--ink);
  }
  .subtitle .highlight { color: var(--accent); font-weight: 600; }
  .author-name {
    position: absolute;
    left: 0;
    top: 1040px;
    width: 100%;
    text-align: center;
    font-family: "Montserrat", sans-serif;
    font-weight: 600;
    font-size: 52px;
    letter-spacing: 0.14em;
    color: var(--ink);
  }
</style>
</head>
<body>
  <main class="book-cover">
    <h1>
      <span class="title title-line-one"><span class="title-small">Rising</span>PAST</span>
      <span class="title title-line-two"><span class="title-small">the</span>WRECK</span>
    </h1>
    <div class="cover-photo" role="img" aria-label="Photo of a judge's wooden gavel resting on its block beside a stethoscope on a bright white surface"></div>
    <p class="subtitle">
      DECODING THE<br>
      <span class="highlight">ACCIDENT CLAIM</span><br>
      PROCESS
    </p>
    <p class="author-name">AUTHOR NAME</p>
  </main>
</body>
</html>
```